Fenwick Chillform Brochure

I would like a simple brochure of very high quality that exudes a prestigious image. The business I run offers a solution for permanent fat loss but is non-invasive and a fraction of the cost of liposuction. I am a sole trader and run a local business from my home. The technology is called Cryolypolysis. It is extremely popular in the US and is breaking in to the UK market. It is virtually pain free, non-invasive, no downtime, and helps people reduce areas with localized fat that do not respond to diet and exercise Ideally, I would like a brochure that folds 3 ways and of very high quality. I offer bespoke services and packages for body scutlping (mulitple treatments to help accentuate mulscle definition). I also have flexible hours for people requiring appointments evenings and weekends. My branding is visible on my website: www.fenwickchillform.example

Target Market(s)

The typical buyer will be someone who is either slightly overweight OR someone who is average and just can't shirt weight in specific areas. It s also useful for people who exercise and want help exposing muscle definition.

Industry/Entity Type

Business

Colors
3176b5
85acd3
33a6d7
ffffff

Requirements
Must have
• I need the following included:
1. The before and after pics
2. The treatable Areas
3. Don't list the prices, but say "Prices start at £400"
4. Do not include Christmas Special as this is temporary
Should not have
• Full price list

```html
<!DOCTYPE html>
<html lang="en">
<head>
<meta charset="utf-8">
<title>Fenwick Chillform – Trifold Brochure</title>
<link rel="stylesheet" href="https://fonts.googleapis.com/css2?family=Cabin:ital,wght@0,400;0,600;0,700;1,400;1,600&display=swap">
<style>
  :root {
    --indigo: #4a5fae;
    --indigo-deep: #3c4f9f;
    --indigo-soft: #8ea3d6;
    --brand-blue: #3176b5;
    --sky: #85acd3;
    --aqua: #33a6d7;
    --white: #ffffff;
    --ink: #333845;
    --muted: #5b6070;
    --backdrop: #a8a8aa;
  }
  * { box-sizing: border-box; margin: 0; padding: 0; }
  html, body { width: 880px; height: 1200px; overflow: hidden; }
  body {
    background: var(--backdrop);
    font-family: "Cabin", sans-serif;
    color: var(--ink);
    position: relative;
  }
  .spread {
    position: absolute;
    left: 20px;
    width: 840px;
    display: flex;
    background: var(--white);
    box-shadow: 0 6px 18px rgba(0,0,0,.22);
  }
  .spread--outside { top: 18px; height: 520px; }
  .spread--inside { top: 570px; height: 612px; }
  .panel { position: relative; width: 280px; height: 100%; overflow: hidden; }
  .panel + .panel { border-left: 1px solid #e6e7ec; }

  /* brand name lockup */
  .brand { display: flex; align-items: center; gap: 8px; justify-content: center; }
  .brand__dot { width: 14px; height: 14px; border-radius: 50%; background: var(--aqua); }
  .brand__name { font-weight: 400; font-size: 20px; color: var(--aqua); }
  .brand--light .brand__dot { background: var(--white); }
  .brand--light .brand__name { color: var(--white); }

  /* outside: back panel */
  .panel--back { display: flex; align-items: center; justify-content: center; background: linear-gradient(90deg, #f4f4f6, #fff); }

  /* outside: contact panel */
  .panel--contact {
    background: linear-gradient(160deg, var(--indigo-deep) 0%, var(--indigo) 45%, var(--indigo-soft) 100%);
    color: var(--white);
    text-align: center;
  }
  .contact__title { font-size: 21px; font-weight: 700; margin-top: 54px; letter-spacing: .3px; }
  .contact__address { font-size: 12.5px; line-height: 1.55; margin-top: 18px; }
  .contact__email { font-size: 13px; font-weight: 600; margin-top: 14px; }
  .contact__phone { font-size: 22px; font-weight: 700; letter-spacing: 1px; margin-top: 4px; }
  .contact__hours { font-size: 12.5px; font-weight: 600; margin-top: 20px; }
  .contact__visual {
    position: absolute; left: 30px; right: 30px; bottom: 26px; height: 220px;
    background: radial-gradient(ellipse at 50% 45%, rgba(200,220,245,.55), rgba(74,95,174,0) 70%);
    display: flex; align-items: flex-end; justify-content: center; padding-bottom: 22px;
  }

  /* outside: cover panel */
  .panel--cover { background: var(--white); display: flex; flex-direction: column; }
  .cover__photo {
    height: 240px; flex: none;
    background: linear-gradient(135deg, #dfe8f3 0%, #f0e6e0 45%, #e9dcd4 70%, #d6e2f0 100%);
  }
  .cover__band { background: var(--indigo); color: var(--white); padding: 12px 14px 8px; }
  .cover__headline { font-size: 17px; font-weight: 700; line-height: 1.15; white-space: nowrap; }
  .cover__sub { font-size: 11.5px; font-style: italic; font-weight: 600; line-height: 1.25; margin-top: 5px; }
  .cover__list { list-style: none; font-size: 9.5px; line-height: 1.6; margin-top: 5px; }
  .cover__list li::before { content: "• "; }
  .cover__extras {
    display: flex; justify-content: space-between; font-size: 9.5px; font-weight: 600; font-style: italic;
    background: var(--indigo-deep); color: var(--white); padding: 6px 14px; white-space: nowrap;
  }
  .cover__brand { flex: 1; display: flex; align-items: center; justify-content: center; }

  /* inside: shared */
  .tab {
    display: inline-block; background: var(--indigo); color: var(--white);
    font-weight: 700; font-size: 13px; letter-spacing: .8px;
    padding: 6px 22px 6px 16px; border-radius: 0 14px 14px 0;
  }
  .panel--inside { padding: 26px 0 0; }
  .panel__body { padding: 0 16px; }

  /* inside: about panel */
  .about__text { font-size: 10px; line-height: 1.5; color: var(--ink); margin-top: 12px; }
  .about__text + .about__text { margin-top: 8px; }
  .about__diagram {
    margin-top: 16px; height: 140px;
    background: linear-gradient(90deg, #e6f1e6, #ecebf4 50%, #e6f1e6);
  }
  .about__captions { display: flex; justify-content: space-around; font-size: 6.5px; color: var(--muted); margin-top: 3px; }
  .results { display: flex; gap: 14px; margin-top: 16px; }
  .result { flex: 1; text-align: center; font-size: 8px; font-weight: 600; color: var(--muted); }
  .result__photo {
    height: 110px; border: 3px solid var(--indigo);
    background: linear-gradient(180deg, #3a3a40 0%, #c9b8a8 45%, #d8c8b8 70%, #4a4656 100%);
    margin-bottom: 4px;
  }

  /* inside: treatable areas panel */
  .areas { list-style: none; margin-top: 16px; }
  .areas li { font-size: 13px; font-weight: 600; color: var(--ink); line-height: 1.7; }
  .areas li::before { content: "•"; margin-right: 6px; }
  .price-note {
    margin-top: 10px; font-size: 16px; font-weight: 700; color: var(--indigo);
    border-top: 1px dotted var(--muted); padding-top: 8px;
  }
  .gallery {
    position: relative; width: 236px; height: 236px; margin: 18px auto 0; border-radius: 50%;
    background: conic-gradient(#d9b9a6 0 60deg, #eae3dc 60deg 120deg, #c9a894 120deg 180deg, #e0c6b5 180deg 240deg, #f1ede8 240deg 300deg, #d2b19c 300deg 360deg);
  }
  .gallery__centre {
    position: absolute; left: 50%; top: 50%; width: 104px; height: 104px; transform: translate(-50%,-50%);
    border-radius: 50%; background: var(--white); display: flex; align-items: center; justify-content: center;
  }
  .gallery__centre .brand__name { font-size: 13px; }
  .gallery__centre .brand__dot { width: 9px; height: 9px; }
  .gallery__centre .brand { gap: 4px; }

  /* inside: faq panel */
  .faq { margin-top: 10px; }
  .faq__item { margin-bottom: 5px; font-size: 7.3px; line-height: 1.32; color: var(--muted); }
  .faq__q { font-weight: 700; color: var(--ink); }
  .testimonial { margin-top: 4px; }
  .testimonial__box {
    margin: 8px 14px 0; border: 3px solid var(--indigo); border-radius: 10px;
    padding: 7px 10px; font-size: 7.3px; font-style: italic; line-height: 1.35; color: var(--ink);
  }
</style>
</head>
<body>

<section class="spread spread--outside" aria-label="Brochure outside">
  <div class="panel panel--back">
    <div class="brand"><span class="brand__dot"></span><span class="brand__name">Chillform</span></div>
  </div>

  <div class="panel panel--contact">
    <h2 class="contact__title">Fenwick Chillform</h2>
    <p class="contact__address">8 Larch Close<br>Fenwick Green<br>Oxfordshire<br>OX9 4QT</p>
    <p class="contact__email">info@fenwickchillform.example</p>
    <p class="contact__phone">07700 900 481</p>
    <p class="contact__hours">Appointments also available evenings &amp; weekends</p>
    <div class="contact__visual" role="img" aria-label="Photograph of stacked clear ice cubes on a blue background">
      <div class="brand brand--light"><span class="brand__dot"></span><span class="brand__name">Chillform</span></div>
    </div>
  </div>

  <div class="panel panel--cover">
    <div class="cover__photo" role="img" aria-label="Photograph of a woman measuring her upper thigh with a tape measure, with frosty sparkles"></div>
    <div class="cover__band">
      <h1 class="cover__headline">Permanent Body Transformation</h1>
      <p class="cover__sub">Body sculpting &amp; permanent fat loss through freezing &amp; destroying fat cells</p>
      <ul class="cover__list">
        <li>Lose 22% - 30% fat in one treatment</li>
        <li>Each treatment in 1 hour</li>
        <li>No pain</li>
        <li>No recovery time</li>
      </ul>
    </div>
    <div class="cover__extras"><span>• Non-invasive treatment</span><span>• Lose up to 30% fat in one session</span></div>
    <div class="cover__brand">
      <div class="brand"><span class="brand__dot"></span><span class="brand__name">Chillform</span></div>
    </div>
  </div>
</section>

<section class="spread spread--inside" aria-label="Brochure inside">
  <div class="panel panel--inside">
    <h2 class="tab">WHAT IS CHILLFORM</h2>
    <div class="panel__body">
      <p class="about__text">Chillform (also known as "Cryolipolysis") was discovered by scientists in 2009. Fat cells are exposed to freezing temperatures and selectively damage and kill fat cells while leaving surrounding cells intact.</p>
      <p class="about__text">By exposing fat cells to low temperatures, they die and the body naturally metabolizes them, while other cells such as skin tissue, blood vessels, and our nervous system are not as sensitive to freezing temperatures and are unaffected.</p>
      <p class="about__text">Over the next 8 weeks, your body eliminates the fat cells leaving you with permanent results.</p>
      <div class="about__diagram" role="img" aria-label="Illustration of an applicator on skin with magnified fat cells before, during and after treatment"></div>
      <div class="about__captions"><span>Before treatment</span><span>During treatment</span><span>After treatment</span></div>
      <div class="results">
        <figure class="result"><div class="result__photo" role="img" aria-label="Before photograph of a torso"></div><figcaption>Before</figcaption></figure>
        <figure class="result"><div class="result__photo" role="img" aria-label="After photograph of a torso following three treatments"></div><figcaption>After 3 treatments</figcaption></figure>
      </div>
    </div>
  </div>

  <div class="panel panel--inside">
    <h2 class="tab">TREATABLE AREAS</h2>
    <div class="panel__body">
      <ul class="areas">
        <li>Back of Arms</li>
        <li>Upper Back (under bra)</li>
        <li>Pectorals</li>
        <li>Love Handles</li>
        <li>Upper Abdomen</li>
        <li>Lower Abdomen</li>
        <li>Inner Thighs</li>
        <li>Rear-Outer Thighs</li>
        <li>Above the knees</li>
      </ul>
      <p class="price-note">Prices start at £400</p>
      <div class="gallery" role="img" aria-label="Circular collage of photographs of treatable body areas: arms, waist, abdomen and thighs">
        <div class="gallery__centre">
          <div class="brand"><span class="brand__dot"></span><span class="brand__name">Chillform</span></div>
        </div>
      </div>
    </div>
  </div>

  <div class="panel panel--inside">
    <h2 class="tab">F.A.Q.</h2>
    <div class="panel__body faq">
      <div class="faq__item"><p class="faq__q">Q: Am I a good candidate?</p><p>A: Good candidates have noticeable bulges in certain areas they'd like to get rid of. Chillform is a fat reduction procedure designed for people with unwanted localised fat that doesn't respond to diet and exercise. It is not a weight loss solution for people who are obese, but a non-surgical alternative to liposuction.</p></div>
      <div class="faq__item"><p class="faq__q">Q: How many treatments will I need?</p><p>A: Depending on your goals, you could need anywhere between 1-3 treatments. You can expect to lose anywhere between 22% to 30% of fat during each treatment.</p></div>
      <div class="faq__item"><p class="faq__q">Q: How long is each session?</p><p>A: Each treatment lasts one hour, and you can treat 2 areas at once. For example: both 'love handles' simultaneously.</p></div>
      <div class="faq__item"><p class="faq__q">Q: Where does the fat go? Are the results permanent?</p><p>A: Once the treated fat cells are crystallised (frozen), the effect on them is permanent and irreversible (cell death). Over time your body processes the fat and eliminates these dead cells.</p></div>
      <div class="faq__item"><p class="faq__q">Q: Is the procedure safe?</p><p>A: Over one million "Cryolipolysis" treatments have been performed worldwide and it is proven to be a safe and effective treatment for non-surgical fat reduction.</p></div>
      <div class="faq__item"><p class="faq__q">Q: Can I return to normal activities after my treatment?</p><p>A: Yes, you can. Chillform is completely non-surgical, so typically you can return to activities immediately afterwards. Patients often return to work after their session.</p></div>
      <div class="faq__item"><p class="faq__q">Q: When will I see results?</p><p>A: You may start to see changes as quickly as three weeks after your treatment, and will experience the most dramatic results after two months. Your body will still flush out fat cells for up to four to six months after treatment.</p></div>
    </div>
    <div class="testimonial">
      <h2 class="tab">TESTIMONIAL</h2>
      <blockquote class="testimonial__box">I've exercised for years and have always stayed in good shape. I eat well and live a healthy lifestyle. No matter what shape I was in, I always had a bulge on my inner thighs. I went to four consultations for liposuction, but could never go through with it. It was too expensive and I would have to tell friends and family so I would have help through the recovery. When I finally found out about Chillform, I had the treatment done right away!! I was able to keep it private and it cost a quarter of the price of liposuction. I saw amazing results within two weeks. It's a year on now, and I still can't believe the shape of my legs! The fat never came back.</blockquote>
    </div>
  </div>
</section>

</body>
</html>
```